DRIFTING PAST LANTERNS - A QUIET HARBOUR

A5 size book of 190 - 210 (70 or 80 gsm wood free paper). The concept revolves around an unseen being that stands on a lotus flower who enters an Indian temple with many of his devotees. Traditional design with photography of a colourful Indian temple is preferred though alternative idea would also be considered. Short narratives at the back of book would give prospective readers an instantaneous insight into the story.

```html
<!DOCTYPE html>
<html lang="en">
<head>
<meta charset="utf-8">
<title>Drifting Past Lanterns – Cover Spread</title>
<link rel="stylesheet" href="https://fonts.googleapis.com/css2?family=Caveat+Brush&family=Cormorant+Garamond:ital,wght@1,400;1,500&family=EB+Garamond:wght@400&display=swap">
<style>
  :root {
    --page-bg: #f1f1f1;
    --sky-cream: #f8ecd0;
    --mist-peach: #f0c9ab;
    --haze-rose: #d9a3a0;
    --hill-mauve: #a06c86;
    --forest-plum: #5a3553;
    --title-plum: #6b3550;
    --author-cream: #fbf0dc;
    --body-ink: #2b1c22;
  }
  * { margin: 0; padding: 0; box-sizing: border-box; }
  html, body {
    width: 899px;
    height: 1200px;
    overflow: hidden;
    background: var(--page-bg);
  }
  .canvas {
    position: relative;
    width: 899px;
    height: 1200px;
  }
  .cover-spread {
    position: absolute;
    left: 20px;
    top: 302px;
    width: 859px;
    height: 595px;
    overflow: hidden;
  }
  .cover-photo {
    position: absolute;
    inset: 0;
    background:
      radial-gradient(ellipse 60% 40% at 88% 5%, var(--sky-cream) 0%, rgba(248,236,208,0) 70%),
      linear-gradient(180deg,
        #f2d9c0 0%,
        var(--mist-peach) 30%,
        var(--haze-rose) 52%,
        var(--hill-mauve) 72%,
        var(--forest-plum) 100%);
  }
  .back-cover {
    position: absolute;
    left: 0;
    top: 0;
    width: 428px;
    height: 100%;
  }
  .back-blurb {
    position: absolute;
    left: 55px;
    top: 58px;
    width: 320px;
    font-family: "EB Garamond", Georgia, serif;
    font-size: 8.6px;
    line-height: 1.36;
    color: var(--body-ink);
    text-align: justify;
    hyphens: auto;
  }
  .back-blurb p + p { margin-top: 10px; }
  .spine {
    position: absolute;
    left: 428px;
    top: 0;
    width: 36px;
    height: 100%;
  }
  .spine-title {
    position: absolute;
    left: 6px;
    top: 28px;
    writing-mode: vertical-rl;
    font-family: "Caveat Brush", cursive;
    font-size: 25px;
    line-height: 1;
    color: var(--title-plum);
    white-space: nowrap;
  }
  .spine-author {
    position: absolute;
    left: 9px;
    top: 346px;
    writing-mode: vertical-rl;
    font-family: "Cormorant Garamond", Georgia, serif;
    font-style: italic;
    font-size: 20px;
    letter-spacing: 9px;
    line-height: 1;
    color: var(--author-cream);
    white-space: nowrap;
  }
  .front-cover {
    position: absolute;
    left: 464px;
    top: 0;
    width: 395px;
    height: 100%;
  }
  .front-title {
    position: absolute;
    left: 40px;
    top: 88px;
    width: 320px;
    font-family: "Caveat Brush", cursive;
    color: var(--title-plum);
    text-align: center;
    line-height: 0.86;
  }
  .front-title .line-main { display: block; font-size: 66px; }
  .front-title .line-small { display: block; font-size: 40px; margin: 2px 0 0 20px; }
  .front-subtitle {
    position: absolute;
    right: 52px;
    top: 236px;
    font-family: "Cormorant Garamond", Georgia, serif;
    font-style: italic;
    font-size: 19px;
    color: var(--title-plum);
  }
  .front-author {
    position: absolute;
    left: 60px;
    top: 528px;
    font-family: "Cormorant Garamond", Georgia, serif;
    font-style: italic;
    font-size: 30px;
    letter-spacing: 9px;
    color: var(--author-cream);
    white-space: nowrap;
  }
</style>
</head>
<body>
<main class="canvas">
  <section class="cover-spread">
    <div class="cover-photo" role="img" aria-label="Misty sunrise over forested hills with a tiered Indian temple on a ridge, in cream, rose and plum tones"></div>

    <div class="back-cover">
      <div class="back-blurb">
        <p>Drifting Past Lanterns follows a traveller who arrives at a hillside harbour town as the evening lamps are lit. Drawn by music from a temple above the mist, she joins a procession of pilgrims and begins a journey that slowly changes how she sees faith, friendship and the quiet work of patience.</p>
        <p>Each chapter is drawn from real days spent walking beside devoted strangers, sharing meals, songs and long silent climbs. Their stories are simple, warm and honest, and together they form a gentle portrait of belonging.</p>
        <p>Written with care and humour, this true account invites readers to slow down, listen closely and notice the small lights that guide us home. It is a book for anyone who has ever wondered where a single step might lead.</p>
      </div>
    </div>

    <div class="spine">
      <span class="spine-title">Drifting Past Lanterns</span>
      <span class="spine-author">Author Name</span>
    </div>

    <div class="front-cover">
      <h1 class="front-title">
        <span class="line-main">Drifting</span>
        <span class="line-small">past</span>
        <span class="line-main">Lanterns</span>
      </h1>
      <p class="front-subtitle">A Quiet Harbour</p>
      <p class="front-author">Author Name</p>
    </div>
  </section>
</main>
</body>
</html>
```